Casa Vantora
Stationery / Business Cards
Professional
Ramiro Quesada
Engineering
427 Brisadores
Suite 392
Laredo, TX
USA
1-800 597-RNQZ
ramiro@casavantora.com.mx
www.casavantora.com.mx
Logo & Website on background
"Control de Iluminacion
Audio y Video Distribuido
Home Theater
Telefonia, Voz y Datos
Integracion de Sistemas
Circuito Cerrado de TV
Ingenieria y Diseno"

```html
<!DOCTYPE html>
<html lang="es">
<head>
<meta charset="utf-8">
<title>Casa Vantora — Stationery</title>
<link rel="stylesheet" href="https://fonts.googleapis.com/css2?family=Open+Sans:wght@400;700&display=swap">
<style>
:root{
  --stage:#d6d6d6;
  --paper:#ffffff;
  --ink:#3a3f47;
  --muted:#8a9099;
  --brand:#1d86c8;
  --brand-deep:#0f4f86;
  --night:#0b0c0e;
  --night-soft:#24272c;
  --rule:#dfe3e8;
}
*{box-sizing:border-box;margin:0;padding:0}
html,body{width:1200px;height:552px;overflow:hidden}
body{background:var(--stage);font-family:"Open Sans",sans-serif;color:var(--ink);position:relative}
.piece{position:absolute;box-shadow:0 2px 6px rgba(0,0,0,.25)}
.brand{display:flex;align-items:center;gap:6px;font-weight:700;color:var(--brand-deep);white-space:nowrap}
.brand-dot{border-radius:50%;background:var(--brand);flex:none}
.tagline{color:var(--brand);font-size:5px;letter-spacing:.2px}
.small{font-size:4.6px;line-height:7px;color:var(--muted)}

/* business cards */
.card{width:92px;height:58px;background:var(--paper);padding:6px}
.card-front-a{left:96px;top:98px;border-top:4px solid var(--brand)}
.card-back-a{left:96px;top:168px;display:flex;flex-direction:column;justify-content:center;align-items:center;border-bottom:5px solid var(--brand)}
.card-front-b{left:96px;top:238px;background:var(--night-soft);border-top:4px solid var(--brand)}
.card-back-b{left:96px;top:306px;background:var(--night);display:flex;align-items:center;justify-content:center}
.card .brand{font-size:7px}
.card .brand-dot{width:9px;height:9px}
.card-front-b .brand,.card-back-b .brand{color:#fff}
.card-front-b .small{color:#b9c0c8}
.card-name{font-size:5.4px;font-weight:700;color:var(--ink)}
.card-front-b .card-name{color:#fff}

/* letterheads */
.letterhead{top:108px;width:221px;height:408px;background:var(--paper);padding:16px 14px}
.letterhead-a{left:206px}
.letterhead-b{left:439px}
.lh-top{display:flex;justify-content:space-between;align-items:flex-start}
.letterhead .brand{font-size:11px}
.letterhead .brand-dot{width:16px;height:16px}
.lh-contact{width:92px}
.lh-mark{position:absolute;left:50%;top:170px;transform:translateX(-50%);display:flex;flex-direction:column;align-items:center;gap:6px;opacity:.08}
.lh-mark .brand-dot{width:70px;height:70px}
.lh-mark span{font-weight:700;font-size:14px;color:var(--brand-deep)}
.lh-lines{position:absolute;left:14px;right:14px;top:92px;height:270px;background:repeating-linear-gradient(to bottom,transparent 0 11px,var(--rule) 11px 12px)}
.lh-bar{position:absolute;left:0;right:0;bottom:0;height:8px;background:linear-gradient(90deg,var(--brand-deep),var(--brand))}

/* folder */
.folder{top:96px;height:420px;width:216px}
.folder-back{left:677px;background:var(--night);display:flex;flex-direction:column;align-items:center;justify-content:center;padding:0 28px}
.folder-front{left:893px;background:var(--paper);display:flex;flex-direction:column;align-items:center;justify-content:center;border-bottom:8px solid var(--brand)}
.folder-back .brand{color:#fff;font-size:10px}
.folder-back .brand-dot{width:14px;height:14px}
.folder-back .small{color:#aab2bc;align-self:stretch;margin-top:8px}
.folder-front .brand{font-size:17px}
.folder-front .brand-dot{width:24px;height:24px}
</style>
</head>
<body>

<!-- business cards -->
<div class="piece card card-front-a">
  <div class="brand"><span class="brand-dot"></span>Casa Vantora</div>
  <p class="card-name" style="margin-top:5px">Ramiro Quesada</p>
  <p class="small">1-800 597-RNQZ<br>ramiro@casavantora.com.mx</p>
</div>
<div class="piece card card-back-a">
  <div class="brand"><span class="brand-dot"></span>Casa Vantora</div>
  <p class="tagline" style="margin-top:3px">Integracion de Sistemas</p>
</div>
<div class="piece card card-front-b">
  <div class="brand"><span class="brand-dot"></span>Casa Vantora</div>
  <p class="card-name" style="margin-top:5px">Ramiro Quesada</p>
  <p class="small">Engineering<br>www.casavantora.com.mx</p>
</div>
<div class="piece card card-back-b">
  <div class="brand"><span class="brand-dot"></span>Casa Vantora</div>
</div>

<!-- letterhead -->
<div class="piece letterhead letterhead-a">
  <div class="lh-top">
    <div>
      <div class="brand"><span class="brand-dot"></span>Casa Vantora</div>
      <p class="tagline" style="margin-top:3px">Integracion de Sistemas</p>
    </div>
    <p class="small lh-contact">427 Brisadores, Suite 392<br>Laredo, TX, USA<br>1-800 597-RNQZ<br>ramiro@casavantora.com.mx<br>www.casavantora.com.mx</p>
  </div>
  <div class="lh-mark"><span class="brand-dot"></span><span>Casa Vantora</span></div>
  <div class="lh-bar"></div>
</div>

<!-- ruled letterhead -->
<div class="piece letterhead letterhead-b">
  <div class="lh-top">
    <div>
      <div class="brand"><span class="brand-dot"></span>Casa Vantora</div>
      <p class="tagline" style="margin-top:3px">Integracion de Sistemas</p>
    </div>
    <p class="small lh-contact">427 Brisadores, Suite 392<br>Laredo, TX, USA<br>1-800 597-RNQZ<br>ramiro@casavantora.com.mx<br>www.casavantora.com.mx</p>
  </div>
  <div class="lh-lines"></div>
  <div class="lh-mark"><span class="brand-dot"></span><span>Casa Vantora</span></div>
  <div class="lh-bar"></div>
</div>

<!-- presentation folder -->
<div class="piece folder folder-back">
  <div class="brand"><span class="brand-dot"></span>Casa Vantora</div>
  <p class="small">427 Brisadores, Suite 392, Laredo, TX, USA<br>1-800 597-RNQZ<br>ramiro@casavantora.com.mx<br>www.casavantora.com.mx</p>
</div>
<div class="piece folder folder-front">
  <div class="brand"><span class="brand-dot"></span>Casa Vantora</div>
  <p class="tagline" style="font-size:7px;margin-top:4px">Integracion de Sistemas</p>
</div>

</body>
</html>
```